Laser Tattoo Removal Business Cards

We are looking for a professional business card design for a laser tattoo removal business. Ideally looking for a black business card design. The name of the business is Brightmoor Ink Erasure. We place our cards at local tattoo shops so we ideally are looking for something trendy/edgy to draw both male and female clientele in.

Target Market(s)

Male/Female ages 18-60

Contact Information for Business Card

black background ideally.. hoping to stay within greys, whites and black

Font styles to use
Serif
Sans Serif

Colors
121212
a9a9a9
5c5c5c
f5f5f5
ffffff
7f7f7f
606060
848484
9d9d9d

Requirements
Must have
• Employee Info:
• Melissa Danforth
• Chief Executive Offer
• m: 919.555.0143
• w: 919.555.0187
• f: 919.555.0162
• mdanforth@brightmoorinkerasure.com
• Address:
• 4518 Pell Ridge Dr, Suite 210
• Raleigh, NC 27699
• Website:
• www.brightmoorinkerasure.com
Nice to have
• Myabe business name on back or logo on back and employee info on the front

```html
<!DOCTYPE html>
<html lang="en">
<head>
<meta charset="utf-8">
<title>Brightmoor Ink Erasure – Business Cards</title>
<link rel="stylesheet" href="https://fonts.googleapis.com/css2?family=Josefin+Sans:wght@600&family=Arimo:wght@400&display=swap">
<style>
  :root {
    --ink: #121212;
    --stage: #2a2a2a;
    --paper: #ffffff;
    --paper-shade: #f5f5f5;
    --grey-dark: #5c5c5c;
    --grey-mid: #7f7f7f;
    --grey-light: #a9a9a9;
    --text-dark: #1a1a1a;
  }
  * { margin: 0; padding: 0; box-sizing: border-box; }
  html, body { width: 1200px; height: 864px; overflow: hidden; }
  body {
    background: var(--stage);
    display: flex;
    flex-direction: column;
    align-items: center;
    justify-content: center;
    gap: 48px;
    font-family: "Arimo", Arial, sans-serif;
  }
  .card {
    position: relative;
    width: 600px;
    height: 343px;
    border-radius: 18px;
    overflow: hidden;
  }
  .card-back { background: var(--ink); }
  .card-front { background: linear-gradient(135deg, var(--paper-shade), var(--paper) 60%); }

  .brand-name {
    font-family: "Josefin Sans", "Helvetica Neue", sans-serif;
    font-weight: 600;
    text-transform: uppercase;
    text-align: center;
    line-height: 1.15;
  }
  .card-back .brand-name {
    position: absolute;
    inset: 0;
    display: flex;
    flex-direction: column;
    justify-content: center;
    color: var(--paper);
    font-size: 44px;
    letter-spacing: 6px;
  }
  .card-front .brand-name {
    position: absolute;
    top: 46px;
    left: 250px;
    width: 320px;
    color: var(--ink);
    font-size: 32px;
    letter-spacing: 4px;
  }

  .wave { position: absolute; inset: 0; }

  .employee {
    position: absolute;
    left: 36px;
    top: 150px;
  }
  .employee-name { font-size: 22px; color: var(--text-dark); }
  .employee-title { font-size: 13px; color: var(--grey-light); margin-top: 2px; }
  .employee-address { font-size: 13px; color: var(--grey-dark); margin-top: 6px; line-height: 1.4; }

  .contact-list {
    position: absolute;
    left: 36px;
    top: 248px;
    list-style: none;
  }
  .contact-list li {
    display: flex;
    align-items: center;
    gap: 8px;
    font-size: 13px;
    color: var(--text-dark);
    height: 19px;
  }
  .contact-list svg { width: 12px; height: 12px; fill: var(--grey-mid); }

  .website {
    position: absolute;
    right: 26px;
    bottom: 22px;
    font-size: 12px;
    color: var(--paper);
    letter-spacing: 0.3px;
  }
</style>
</head>
<body>

  <section class="card card-back" aria-label="Card back">
    <div class="brand-name"><span>Brightmoor</span><span>Ink Erasure</span></div>
  </section>

  <section class="card card-front" aria-label="Card front">
    <svg class="wave" viewBox="0 0 600 343" preserveAspectRatio="none" aria-hidden="true">
      <path d="M600 150 C560 150 520 160 515 185 C510 215 480 225 450 232 C400 245 370 290 355 343 L600 343 Z" fill="var(--ink)"/>
    </svg>

    <div class="brand-name"><div>Brightmoor</div><div>Ink Erasure</div></div>

    <div class="employee">
      <div class="employee-name">Melissa Danforth</div>
      <div class="employee-title">Chief Executive Offer</div>
      <div class="employee-address">4518 Pell Ridge Dr, Suite 210<br>Raleigh, NC 27699</div>
    </div>

    <ul class="contact-list">
      <li>
        <svg viewBox="0 0 12 12" aria-label="Mobile"><path d="M3 0h6a1 1 0 0 1 1 1v10a1 1 0 0 1-1 1H3a1 1 0 0 1-1-1V1a1 1 0 0 1 1-1zm0 2v7h6V2zm3 8a.6.6 0 1 0 0 1.2A.6.6 0 0 0 6 10z"/></svg>
        919.555.0143
      </li>
      <li>
        <svg viewBox="0 0 12 12" aria-label="Work phone"><path d="M2.5 0.5l2 2.2-1 1.3c.8 1.7 2 2.9 3.6 3.7l1.3-1 2.2 2-1.2 1.8C5 10.3 1.6 6.9.8 1.7z"/></svg>
        919.555.0187
      </li>
      <li>
        <svg viewBox="0 0 12 12" aria-label="Fax"><path d="M3 0h5l1 1v3H3zM1 4.5h10a1 1 0 0 1 1 1V10H0V5.5a1 1 0 0 1 1-1zM3 8h6v4H3z"/></svg>
        919.555.0162
      </li>
      <li>
        <svg viewBox="0 0 12 12" aria-label="Email"><path d="M0 2h12v8H0zm1 1v.4l5 3.3 5-3.3V3zm0 1.6V9h10V4.6L6 8z"/></svg>
        mdanforth@brightmoorinkerasure.com
      </li>
    </ul>

    <div class="website">www.brightmoorinkerasure.com</div>
  </section>

</body>
</html>
```